Marlow Family Chiropractic Stationary

The letterhead and business card must have our logo.
We would like to see the logo used in different ways ( It can be expanded upon in the stationary.)
Please use the the same or similar colors.
Must be eye catching and memorable.
Must be easy to read

Reason: The doctor has been too busy to make any final decisions. He would like to give himself a little more time.

Target Market(s)

Chiropractic Healthcare

Industry/Entity Type

Business

Requirements
Must have
• Dr. Nathaniel Marlow D.C.
Chiropractor

860-555-0193

415 Birchwood Parkway, Suite 3
Hollis Bay, ME 04099

drmarlow@marlowspine.example
www.marlowspine.example
www.friendpage.example/MarlowFamilySpine
Should not have
• should not be difficult to read

```html
<!DOCTYPE html>
<html lang="en">
<head>
<meta charset="utf-8">
<title>Marlow Family Chiropractic Stationery</title>
<link href="https://fonts.googleapis.com/css2?family=Open+Sans:wght@300;400;600;700&family=Roboto+Condensed:wght@400&display=swap" rel="stylesheet">
<style>
  :root{
    --backdrop:#e9e6e1;
    --paper:#ffffff;
    --card-white:#f4f4f4;
    --brand-green:#3f9e16;
    --green-light:#5cbd22;
    --green-deep:#2d8509;
    --green-strip:#1f5e08;
    --ink:#444444;
    --ink-soft:#555555;
    --shadow:0 2px 6px rgba(0,0,0,.35);
  }
  *{box-sizing:border-box;margin:0;padding:0}
  html,body{width:1200px;height:917px;overflow:hidden;background:var(--backdrop)}
  .canvas{position:relative;width:1200px;height:917px;font-family:"Open Sans",Arial,sans-serif;color:var(--ink)}

  .letterhead{position:absolute;left:65px;top:25px;width:669px;height:864px;background:var(--paper);box-shadow:var(--shadow)}
  .letterhead__band{position:absolute;left:0;bottom:0;width:100%;height:19px;background:var(--brand-green)}

  .brand{position:absolute;display:flex;flex-direction:column;align-items:center;text-align:center;transform:translateX(-50%)}
  .brand__dot{border-radius:50%;background:var(--brand-green)}
  .brand__name{font-family:"Open Sans",Arial,sans-serif;font-weight:700;color:var(--brand-green);line-height:1.2;text-transform:uppercase;white-space:nowrap}
  .letterhead .brand{left:95px;top:30px}
  .letterhead .brand__dot{width:66px;height:66px;margin-bottom:8px}
  .letterhead .brand__name{font-size:10px}

  .contact{position:absolute;list-style:none;font-family:"Open Sans",Arial,sans-serif;color:var(--ink)}
  .contact li{display:flex;align-items:flex-start;gap:6px;line-height:1.2;white-space:nowrap}
  .contact svg{flex:none;width:8px;height:8px;margin-top:1px;fill:var(--brand-green)}
  .letterhead .contact{left:469px;top:52px;font-size:8.6px}
  .letterhead .contact li{margin-bottom:4px}

  .letter{position:absolute;left:79px;top:222px;width:494px;font-size:12.3px;font-weight:300;line-height:15.4px;color:var(--ink-soft)}
  .letter p{margin-bottom:15.4px}
  .letter .date{margin-bottom:10px}
  .letter address{font-style:normal;margin-bottom:26px}
  .letter .salutation{margin-bottom:15px}
  .letter .body{text-align:justify;margin-bottom:16px}
  .letter .closing{margin-top:24px}

  .card{position:absolute;left:762px;width:378px;height:218px;box-shadow:var(--shadow);overflow:hidden}
  .card--front{top:233px;background:radial-gradient(ellipse at 50% 45%,var(--green-light) 0%,var(--brand-green) 55%,var(--green-deep) 100%)}
  .card--front .brand{left:189px;top:30px}
  .card--front .brand__dot{width:72px;height:72px;margin-bottom:10px;background:#ffffff}
  .card--front .brand__name{color:#ffffff;font-size:11.5px}
  .card__strip{position:absolute;left:0;bottom:0;width:100%;height:28px;background:var(--green-strip);color:#ffffff;font-size:11px;font-weight:600;text-align:center;line-height:28px}

  .card--back{top:463px;background:linear-gradient(180deg,#fbfbfb 0%,var(--card-white) 100%)}
  .card--back .brand{left:86px;top:42px}
  .card--back .brand__dot{width:66px;height:66px;margin-bottom:10px}
  .card--back .brand__name{font-size:9.5px}
  .card__divider{position:absolute;left:166px;top:43px;width:1px;height:137px;background:var(--brand-green)}
  .card__name{position:absolute;left:182px;top:44px;font-family:"Roboto Condensed",Arial,sans-serif;font-weight:400;font-size:15.5px;color:var(--brand-green)}
  .card__title{position:absolute;right:28px;top:70px;font-family:"Roboto Condensed",Arial,sans-serif;font-size:11.5px;color:var(--ink)}
  .card--back .contact{left:186px;top:96px;font-size:8.2px}
  .card--back .contact li{margin-bottom:6px}
</style>
</head>
<body>
<svg width="0" height="0" style="position:absolute" aria-hidden="true">
  <symbol id="icon-phone" viewBox="0 0 10 10"><path d="M2 1h2l1 2.2-1.2.9c.6 1.2 1.4 2 2.6 2.6l.9-1.2L9.5 6.6V8.6c0 .5-.4.9-.9.9C4.5 9.4.6 5.5.5 1.5c0-.3.3-.5.6-.5z"/></symbol>
  <symbol id="icon-mail" viewBox="0 0 10 10"><path d="M.5 2h9v6h-9zM1.2 2.6 5 5.6l3.8-3z" fill-rule="evenodd"/></symbol>
  <symbol id="icon-globe" viewBox="0 0 10 10"><path d="M5 .5a4.5 4.5 0 1 0 0 9 4.5 4.5 0 0 0 0-9zm0 1.1c.6.6 1 1.6 1.1 2.9H3.9C4 3.2 4.4 2.2 5 1.6zM1.6 5.5h1.3c.1 1 .3 1.8.7 2.4A3.4 3.4 0 0 1 1.6 5.5zm0-1a3.4 3.4 0 0 1 2-2.4c-.4.6-.6 1.4-.7 2.4zM5 8.4c-.6-.6-1-1.6-1.1-2.9h2.2C6 6.8 5.6 7.8 5 8.4zm1.4-.5c.4-.6.6-1.4.7-2.4h1.3a3.4 3.4 0 0 1-2 2.4zm.7-3.4c-.1-1-.3-1.8-.7-2.4a3.4 3.4 0 0 1 2 2.4z"/></symbol>
  <symbol id="icon-square" viewBox="0 0 10 10"><rect x="1" y="1" width="8" height="8" rx="1"/></symbol>
  <symbol id="icon-pin" viewBox="0 0 10 10"><path d="M5 .5a3.2 3.2 0 0 0-3.2 3.2C1.8 6 5 9.5 5 9.5S8.2 6 8.2 3.7A3.2 3.2 0 0 0 5 .5zm0 4.5a1.3 1.3 0 1 1 0-2.6 1.3 1.3 0 0 1 0 2.6z"/></symbol>
</svg>

<main class="canvas">
  <section class="letterhead">
    <div class="brand">
      <span class="brand__dot"></span>
      <span class="brand__name">Marlow<br>Family Chiropractic</span>
    </div>
    <ul class="contact">
      <li><svg><use href="#icon-phone"/></svg>860-555-0193</li>
      <li><svg><use href="#icon-mail"/></svg>drmarlow@marlowspine.example</li>
      <li><svg><use href="#icon-globe"/></svg>www.marlowspine.example</li>
      <li><svg><use href="#icon-square"/></svg>www.friendpage.example/MarlowFamilySpine</li>
      <li><svg><use href="#icon-pin"/></svg><span>415 Birchwood Parkway, Suite 3<br>Hollis Bay, ME 04099</span></li>
    </ul>
    <article class="letter">
      <p class="date">April 10, 2010</p>
      <address>Alan Pierce<br>88 Linden Avenue<br>Buffalo, New York 14201</address>
      <p class="salutation">Dear Alan Pierce,</p>
      <p class="body">Luptiunda deliquiati quatem quiam hit que paribusandic tectate perum eriaece pratur si te dolorem volore sequo tem resequae cus sequaerundit la dolupti remolor emporionest as assit que litis nonsent aut ea cus. Musantum imintempos esequis essunt ut et qui omnis ea il illest quaspis ex esto quas assimus, sint laborio. Facepe si occus etur, nisque cus soluptin praepudit re, soloremquae. Berum sitemped molo coritas imagnitaque niminis pro et et faccum adi optatem ea dis soluptatis et fuga.</p>
      <p class="body">Es aut et utectae essita quas et ut estis apel magnati aut ad maio volendu ntotatur rem diatest, as sum ea sum re qui rerspit quam esenecu llabo. Andit, auta dolorep editam facea cus et occab ium et que mintor re eum ut poritione volende bitaeria velia que imus et liciis sum nobita voloreic tem et quod quam sum doluptatum fugit fugit atiuste dolestrunti cus esedi bearchi lloreptatume volupit, unt. Ictenimusa dunto modisit latiae officaepe pora cor si repraerci odit, iminullut restem assit, comnim ut autatiis dolorioratur sitin conseque evella velitio te ad quid quiandios doles autat etur? Ra que doluptaturio blab il ipsa nobit la volupicae. Aruptassinus eres a pe dolupie niminto et, aborro totatius nossi sequia vollupt ibust, officidebis es debiscienda sum ullam que voluptatur, alitat. It quuntium si cus atem. Nem venimus tinullique quiate ma iusaped ut aut molorem poreper</p>
      <p class="body">Si consequae omnis nonse quist alitamus erum aspedis inctiam rem ex et, utem unt, quam es sitates nus denim volest ex et et in natium estis volest.</p>
      <p class="closing">Sincerely,</p>
    </article>
    <div class="letterhead__band"></div>
  </section>

  <section class="card card--front">
    <div class="brand">
      <span class="brand__dot"></span>
      <span class="brand__name">Marlow<br>Family Chiropractic</span>
    </div>
    <div class="card__strip">www.marlowspine.example</div>
  </section>

  <section class="card card--back">
    <div class="brand">
      <span class="brand__dot"></span>
      <span class="brand__name">Marlow<br>Family Chiropractic</span>
    </div>
    <div class="card__divider"></div>
    <h2 class="card__name">Dr. Nathaniel Marlow D.C.</h2>
    <p class="card__title">Chiropractor</p>
    <ul class="contact">
      <li><svg><use href="#icon-phone"/></svg>860-555-0193</li>
      <li><svg><use href="#icon-mail"/></svg>drmarlow@marlowspine.example</li>
      <li><svg><use href="#icon-globe"/></svg>www.marlowspine.example</li>
      <li><svg><use href="#icon-square"/></svg>www.friendpage.example/MarlowFamilySpine</li>
      <li><svg><use href="#icon-pin"/></svg><span>415 Birchwood Parkway, Suite 3<br>Hollis Bay, ME 04099</span></li>
    </ul>
  </section>
</main>
</body>
</html>
```